Unique Business Card Design

Unique Business Card design for our orthotic and prosthetic company. Our logo is on our website, color is light blue. Unique shape (artificial leg shaped, vertical, etc..) preferred. Logo, business name, individual name and basic demographics needed.

Industry/Entity Type

Business

Contact Information for Business Card

Logo, Industry, Phone # Logo, "Prosthetic & Orthotic Services" Place to add individual name and contact info

Colors
cee9f5

Requirements
Must have
• The icon must be there, placement of "Prosthetic & Orthotic Services" can be moved
Nice to have
• Like the mix of light blue, and a little darker blue. One design included the icons from my website which was a nice touch

```html
<!DOCTYPE html>
<html lang="en">
<head>
<meta charset="UTF-8">
<title>Limbworks Inc. Business Card</title>
<link rel="stylesheet" href="https://fonts.googleapis.com/css2?family=Playfair+Display:ital@1&family=Roboto:wght@400;700&display=swap">
<style>
  :root {
    --brand-blue: #0a5eb0;
    --card-white: #ffffff;
    --ink: #1c1c1c;
    --stage: #e6e8eb;
  }
  * { margin: 0; padding: 0; box-sizing: border-box; }
  html, body {
    width: 1200px;
    height: 892px;
    overflow: hidden;
    background: var(--stage);
  }
  .canvas {
    width: 1200px;
    height: 892px;
    display: flex;
    align-items: center;
    justify-content: center;
  }
  .card {
    position: relative;
    width: 500px;
    height: 820px;
    background: var(--brand-blue);
    overflow: hidden;
    box-shadow: 0 10px 30px rgba(0,0,0,0.18);
    font-family: "Roboto", sans-serif;
  }
  .card__circle {
    position: absolute;
    left: 50%;
    top: 50%;
    width: 648px;
    height: 648px;
    margin-left: -324px;
    margin-top: -324px;
    border-radius: 50%;
    background: var(--card-white);
  }
  .card__tagline {
    position: absolute;
    top: 30px;
    left: 0;
    right: 0;
    text-align: center;
    font-family: "Playfair Display", serif;
    font-style: italic;
    font-size: 30px;
    color: var(--card-white);
  }
  .card__content {
    position: absolute;
    top: 150px;
    left: 0;
    right: 0;
    text-align: center;
    color: var(--ink);
  }
  .brand__mark {
    width: 118px;
    height: 118px;
    border-radius: 50%;
    background: var(--brand-blue);
    margin: 0 auto 14px;
  }
  .brand__name {
    font-size: 40px;
    font-weight: 700;
    color: var(--brand-blue);
    letter-spacing: 0.5px;
    margin-bottom: 34px;
  }
  .person__name {
    font-size: 32px;
    line-height: 1.1;
  }
  .person__title,
  .person__phone {
    font-size: 23px;
    line-height: 1.3;
  }
  .office {
    margin-top: 36px;
    font-size: 23px;
    line-height: 1.35;
  }
  .card__address {
    position: absolute;
    bottom: 18px;
    left: 0;
    right: 0;
    text-align: center;
    color: var(--card-white);
    font-size: 24px;
    line-height: 1.25;
  }
</style>
</head>
<body>
  <main class="canvas">
    <article class="card">
      <div class="card__circle"></div>
      <p class="card__tagline">Prosthetic &amp; Orthotic Services</p>
      <div class="card__content">
        <div class="brand__mark"></div>
        <p class="brand__name">LIMBWORKS INC.</p>
        <p class="person__name">Mira Castellan</p>
        <p class="person__title">Orthotist / Prosthetist</p>
        <p class="person__phone">555-204-3318</p>
        <div class="office">
          <p class="office__phone">555-860-2240</p>
          <p class="office__email">limbworks@mailhub.net</p>
          <p class="office__web">www.limbworks-care.com</p>
        </div>
      </div>
      <address class="card__address" style="font-style: normal;">
        820 Harbor Row<br>Westbrook, NY 11000
      </address>
    </article>
  </main>
</body>
</html>
```